Kestrel Bridge Consulting (KBC) Business Card Design

I would like to create double-sided business cards that contain:
1) Name: Derek Molvane
2) Phone Number: +1 (555) 218-4907
3) Email: Derek.Molvane@KestrelBridgeConsulting.example
4) Website: KestrelBridgeConsulting.example

I would like to include my logo and a color scheme similar to the Varnholt Grand Prix Ostera squad color scheme (black, silver, greenish-blue – but can also include regular blue)

What we do: Our company develops and delivers innovative and pragmatic information technology and cybersecurity risk and compliance solutions for organizations in the commercial market as well as the federal, and state/local sectors.

```html
<!DOCTYPE html>
<html lang="en">
<head>
<meta charset="utf-8">
<title>Kestrel Bridge Consulting – Business Card</title>
<link rel="stylesheet" href="https://fonts.googleapis.com/css2?family=Michroma&family=Lato:wght@400;700;900&display=swap">
<style>
  :root {
    --page: #e9e6e2;
    --card: #2a2a2a;
    --card-tone: #303030;
    --ink: #ffffff;
    --accent: #19a9e6;
    --rule: #bdbdbd;
  }
  * { box-sizing: border-box; margin: 0; padding: 0; }
  html, body { width: 1200px; height: 901px; overflow: hidden; }
  body {
    background: var(--page);
    position: relative;
    font-family: "Lato", sans-serif;
    color: var(--ink);
  }
  .card {
    position: absolute;
    left: 290px;
    width: 620px;
    height: 354px;
    background: var(--card);
    box-shadow: 0 6px 18px rgba(0,0,0,0.25);
    overflow: hidden;
  }
  .card--front { top: 66px; }
  .card--back { top: 481px; }

  /* Front */
  .lockup {
    position: absolute;
    left: 50%;
    top: 50%;
    transform: translate(-50%, -50%);
    display: flex;
    align-items: center;
    gap: 16px;
  }
  .lockup__mark {
    width: 64px; height: 64px;
    border-radius: 50%;
    background: var(--accent);
  }
  .lockup__rule {
    width: 1px; height: 68px;
    background: var(--rule);
  }
  .wordmark {
    font-family: "Michroma", sans-serif;
    text-transform: uppercase;
    color: var(--ink);
    line-height: 1.05;
    letter-spacing: 0.04em;
  }
  .lockup .wordmark { font-size: 17px; }

  /* Back */
  .backdrop-mark {
    position: absolute;
    right: -40px;
    top: 20px;
    width: 300px; height: 300px;
    border-radius: 50%;
    background: var(--card-tone);
  }
  .card--back .wordmark {
    position: absolute;
    left: 52px;
    top: 70px;
    font-size: 25px;
  }
  .person {
    position: absolute;
    left: 110px;
    top: 200px;
  }
  .person__name {
    font-weight: 900;
    font-size: 26px;
    color: var(--accent);
    letter-spacing: -0.01em;
  }
  .person__role {
    font-size: 11px;
    margin: 2px 0 0 14px;
  }
  .contact {
    list-style: none;
    position: absolute;
    left: 134px;
    top: 276px;
    font-size: 12px;
    line-height: 1.55;
  }
  .contact li { display: flex; align-items: center; gap: 8px; }
  .contact svg { width: 11px; height: 11px; fill: var(--accent); flex: none; }
</style>
</head>
<body>
  <section class="card card--front" aria-label="Card front">
    <div class="lockup">
      <span class="lockup__mark"></span>
      <span class="lockup__rule"></span>
      <p class="wordmark">Kestrel<br>Bridge<br>Consulting</p>
    </div>
  </section>

  <section class="card card--back" aria-label="Card back">
    <span class="backdrop-mark"></span>
    <p class="wordmark">Kestrel<br>Bridge<br>Consulting</p>
    <div class="person">
      <p class="person__name">Derek Molvane</p>
      <p class="person__role">Manager</p>
    </div>
    <ul class="contact">
      <li>
        <svg viewBox="0 0 24 24" aria-hidden="true"><path d="M6.6 10.8a15 15 0 0 0 6.6 6.6l2.2-2.2c.3-.3.7-.4 1-.2 1.1.4 2.3.6 3.6.6.6 0 1 .4 1 1V20c0 .6-.4 1-1 1A17 17 0 0 1 3 4c0-.6.4-1 1-1h3.5c.6 0 1 .4 1 1 0 1.3.2 2.5.6 3.6.1.3 0 .7-.2 1z"/></svg>
        +1 (555) 218-4907
      </li>
      <li>
        <svg viewBox="0 0 24 24" aria-hidden="true"><path d="M2 5h20v14H2z M2 5l10 8 10-8" /></svg>
        Derek.Molvane@KestrelBridgeConsulting.example
      </li>
      <li>
        <svg viewBox="0 0 24 24" aria-hidden="true"><circle cx="12" cy="12" r="10"/></svg>
        KestrelBridgeConsulting.example
      </li>
    </ul>
  </section>
</body>
</html>
```